" Atendemos de maneira integrada em reabilitação ,tanto odontológica como neurológica. Somos terapia ocupacional, fonoaudiologia, neuropediatria e odontologia. Trabalhamos com técnicas de ponta e muito proximidade com nossos pacientes e suas famílias. "

```html
<!DOCTYPE html>
<html lang="pt-BR">
<head>
<meta charset="UTF-8">
<title>Elomar — Papel Timbrado</title>
<link href="https://fonts.googleapis.com/css2?family=Montserrat:wght@400;600;700&display=swap" rel="stylesheet">
<style>
  :root {
    --bg: #e9eaec;
    --paper: #ffffff;
    --teal: #2a9bb8;
    --teal-dark: #1f7f99;
    --green: #8cc63f;
    --text: #4a5a6a;
    --ghost: #eef1f6;
  }
  * { margin: 0; padding: 0; box-sizing: border-box; }
  html, body { width: 1200px; height: 1200px; overflow: hidden; }
  body {
    background: var(--bg);
    font-family: "Montserrat", Arial, sans-serif;
    display: flex; align-items: center; justify-content: center;
  }
  .letterhead {
    position: relative;
    width: 760px; height: 1075px;
    background: var(--paper);
    box-shadow: 0 6px 24px rgba(0,0,0,0.12);
    overflow: hidden;
  }
  .letterhead__frame { position: absolute; inset: 0; }
  .brand {
    position: absolute; top: 62px; right: 62px;
    text-align: right;
  }
  .brand__row { display: flex; align-items: center; gap: 8px; justify-content: flex-end; }
  .brand__square { width: 12px; height: 12px; background: var(--green); }
  .brand__name {
    font-weight: 600; font-size: 24px; letter-spacing: 0.5px; color: var(--teal);
  }
  .brand__tagline {
    margin-top: 5px; font-size: 8px; letter-spacing: 0.6px; color: var(--text);
    text-transform: uppercase;
  }
  .watermark {
    position: absolute; left: 230px; top: 330px;
    width: 300px; height: 280px; border-radius: 45% 55% 40% 60%;
    background: radial-gradient(circle, var(--ghost) 0%, rgba(238,241,246,0) 75%);
  }
  .contacts {
    position: absolute; left: 48px; right: 48px; bottom: 118px;
    display: flex; justify-content: space-between;
    font-size: 11px; color: var(--text);
  }
  .contacts__item { display: flex; align-items: center; gap: 7px; }
  .contacts__icon { width: 14px; height: 14px; }
</style>
</head>
<body>
  <div class="letterhead">
    <svg class="letterhead__frame" width="760" height="1075" viewBox="0 0 760 1075">
      <path d="M0 14 C 250 22, 560 10, 760 0" fill="none" stroke="var(--green)" stroke-width="5"/>
      <path d="M0 978 C 260 990, 520 1010, 760 950 L760 1075 L0 1075 Z" fill="var(--green)"/>
      <path d="M0 990 C 260 1000, 520 1020, 760 966 L760 1075 L0 1075 Z" fill="var(--teal)"/>
      <path d="M0 1030 C 260 1040, 520 1050, 760 1010 L760 1075 L0 1075 Z" fill="var(--teal-dark)" opacity="0.35"/>
    </svg>

    <div class="brand">
      <div class="brand__row">
        <span class="brand__square"></span>
        <span class="brand__name">Elomar</span>
      </div>
      <div class="brand__tagline">Clínica de Reabilitação Integrada</div>
    </div>

    <div class="watermark" role="img" aria-label="Faint brand symbol decoration"></div>

    <div class="contacts">
      <div class="contacts__item">
        <svg class="contacts__icon" viewBox="0 0 14 14"><circle cx="7" cy="7" r="7" fill="var(--teal)"/><path d="M7 3.2a2.3 2.3 0 0 0-2.3 2.3C4.7 7.3 7 10.5 7 10.5s2.3-3.2 2.3-5A2.3 2.3 0 0 0 7 3.2z" fill="#fff"/></svg>
        <span>Rua das Acácias, 120</span>
      </div>
      <div class="contacts__item">
        <svg class="contacts__icon" viewBox="0 0 14 14"><circle cx="7" cy="7" r="7" fill="var(--teal)"/><path d="M4.6 3.6l1.3 1.7-.7.9c.5 1 1.3 1.8 2.3 2.3l.9-.7 1.7 1.3-.7 1.1C7 10.2 3.8 7 3.5 4.3z" fill="#fff"/></svg>
        <span>(11) 4002-3150</span>
      </div>
      <div class="contacts__item">
        <svg class="contacts__icon" viewBox="0 0 14 14"><circle cx="7" cy="7" r="7" fill="var(--teal)"/><rect x="3.6" y="4.6" width="6.8" height="4.8" fill="#fff"/><path d="M3.6 4.6L7 7.3l3.4-2.7" fill="none" stroke="var(--teal)" stroke-width="0.8"/></svg>
        <span>contato@elomar.com.br</span>
      </div>
    </div>
  </div>
</body>
</html>
```